New corporate stationery design for UK train leasing company

In advance of an office move later this year we are looking to redesign all our corporate stationery (business cards, letterhead, compliment slips, envelopes etc) as well as small branded items (such as mouse mats, drink mats, etc).

We wish to keep the same logo and corporate colours but are looking for a modern, fresh look that will tie in our stationery more with the look of our website and our PowerPoint template. We have a strapline, "Track Crews, True Knowhow" that we would like to incorporate into the stationery design and also need to include a "TEMLO" logo on the bottom of the letterhead/compliment slips. We have two offices so will need letterhead and compliment slips with both addresses.

The files attached include different versions of our logo (the main one is the black with green halo, file 1 or 3), our brand guidelines summary (including Pantone colours), the TEMLO logo and PowerPoint template.

More information about the business can be found at www.fernholtrail.co.uk.

If you have any questions please let me know.

I look forward to seeing the designs!
Regards
Moira

Target Market(s)

Main audience are train operators, rail industry suppliers, passenger transport groups, government and other political organisations, financiers/lenders.

Industry/Entity Type

Business

```html
<!DOCTYPE html>
<html lang="en">
<head>
<meta charset="utf-8">
<title>Fernholt Rail – Stationery Set</title>
<link href="https://fonts.googleapis.com/css2?family=Quicksand:wght@400;500&family=Arimo:wght@400;700&display=swap" rel="stylesheet">
<style>
  :root{
    --bg:#eceeed;
    --paper:#ffffff;
    --charcoal:#4a4a4b;
    --teal:#0aa08d;
    --ink:#3c3c3c;
    --muted:#777777;
    --brand-font:"Quicksand", sans-serif;
    --body-font:"Arimo", sans-serif;
  }
  *{box-sizing:border-box;margin:0;padding:0}
  html,body{width:1200px;height:937px;overflow:hidden;background:var(--bg)}
  .canvas{position:relative;width:1200px;height:937px}
  .sheet{position:absolute;background:var(--paper);box-shadow:0 2px 6px rgba(0,0,0,.18);overflow:hidden}

  .brand{position:absolute;display:flex;align-items:center;gap:.25em;font-family:var(--brand-font);font-weight:400;color:var(--charcoal);white-space:nowrap;letter-spacing:-.01em;line-height:1}
  .brand .dot{width:.32em;height:.32em;border-radius:50%;background:var(--teal);flex:none}
  .brand--light{color:#ffffff}

  .web{position:absolute;font-family:var(--brand-font);font-weight:500;letter-spacing:.2em;white-space:nowrap}
  .icon{position:absolute;border-radius:50%;background:var(--teal);display:flex;align-items:center;justify-content:center}
  .icon svg{width:60%;height:60%}

  /* Letterhead */
  .letterhead{left:185px;top:68px;width:389px;height:544px}
  .letterhead .band{position:absolute;left:0;top:0;width:28px;height:100%;background:var(--charcoal)}
  .letterhead .brand{left:42px;top:32px;font-size:21px}
  .letter{position:absolute;left:36px;top:138px;width:300px;font-family:var(--body-font);font-size:5.4px;line-height:7.2px;color:var(--ink)}
  .letter p{margin-bottom:8px}
  .letter .gap{margin-bottom:20px}
  .signature{width:26px;height:18px;margin:2px 0 6px;background:linear-gradient(90deg,#d6d6d6,#bdbdbd);border-radius:2px}
  .letter strong{font-weight:700}
  .lh-contact{position:absolute;left:40px;font-family:var(--body-font);font-size:4.6px;line-height:6px;color:var(--ink)}

  /* Folder */
  .folder{left:636px;top:41px;width:458px;height:575px;background:var(--charcoal)}
  .folder .strip{position:absolute;left:0;top:0;width:45px;height:100%;background:var(--teal)}
  .folder .brand{left:88px;top:250px;font-size:52px}
  .folder .web{left:60px;top:529px;font-size:12px;color:#ffffff}

  /* Business cards */
  .card-front{left:46px;top:658px;width:176px;height:100px}
  .card-front .brand{left:94px;top:29px;font-size:12.5px}
  .card-contact{position:absolute;right:112px;font-family:var(--body-font);font-size:4.2px;line-height:5.4px;color:#ffffff;text-align:right}
  .card-name{position:absolute;right:10px;top:78px;font-family:var(--body-font);font-size:6px;color:var(--ink);text-align:right;line-height:7px}
  .card-back{left:46px;top:785px;width:176px;height:99px}
  .card-back .brand{left:34px;top:41px;font-size:16px}

  /* Compliment slip */
  .slip{left:265px;top:672px;width:430px;height:208px}
  .slip .band{position:absolute;left:0;top:0;width:24px;height:100%;background:var(--charcoal)}
  .slip .brand{left:34px;top:24px;font-size:21px}
  .slip .address{position:absolute;left:34px;top:68px;font-family:var(--body-font);font-size:7px;color:var(--ink)}
  .slip .web{left:36px;top:182px;font-size:10px;color:var(--charcoal)}

  /* Envelope back */
  .envelope{left:737px;top:671px;width:434px;height:209px}
  .envelope .flap{position:absolute;left:0;top:0;width:100%;height:72px;background:var(--charcoal);border-radius:0 0 40px 40px}
  .envelope .web{left:0;right:0;top:30px;text-align:center;font-size:13px;color:#ffffff}
</style>
</head>
<body>
<main class="canvas">

  <!-- Letterhead -->
  <section class="sheet letterhead" aria-label="Letterhead">
    <div class="band"></div>
    <div class="brand">fernholt rail<span class="dot"></span></div>
    <div class="letter">
      <p>July 2, 2012</p>
      <p><strong>Dear Sir,</strong><br>Harrow House, Canal St., London</p>
      <p class="gap">Thank you for your interest in our leasing services. Our team has supported train operators across the country for many years, providing modern fleets, careful maintenance planning and dependable advice. We would welcome the chance to meet and discuss how our rolling stock can meet your timetable, budget and growth plans in the years ahead.</p>
      <p class="gap">Please find enclosed a summary of current fleet availability and indicative terms for your review.</p>
      <p>Should you have any questions, our commercial team will be happy to arrange a visit to one of our depots or offices. We value long partnerships built on trust, clear communication and shared standards of safety, and we look forward to hearing from you soon.</p>
      <p>Best Regards,</p>
      <div class="signature" role="img" aria-label="Handwritten signature"></div>
      <p><strong>Daniel Orme</strong><br>Director<br><br>Harrow House, Canal St., London</p>
    </div>

    <div class="icon" style="left:20px;top:466px;width:15px;height:15px">
      <svg viewBox="0 0 24 24" fill="#fff"><path d="M6.6 10.8a15 15 0 006.6 6.6l2.2-2.2c.3-.3.7-.4 1-.2 1.1.4 2.3.6 3.6.6.6 0 1 .4 1 1V20c0 .6-.4 1-1 1A17 17 0 013 4c0-.6.4-1 1-1h3.5c.6 0 1 .4 1 1 0 1.3.2 2.5.6 3.6.1.3 0 .7-.2 1z"/></svg>
    </div>
    <div class="lh-contact" style="top:468px">020 7946 0142<br>020 7946 0143</div>
    <div class="icon" style="left:20px;top:487px;width:15px;height:15px">
      <svg viewBox="0 0 24 24" fill="#fff"><path d="M12 2a7 7 0 00-7 7c0 5 7 13 7 13s7-8 7-13a7 7 0 00-7-7zm0 9.5A2.5 2.5 0 1112 6a2.5 2.5 0 010 5.5z"/></svg>
    </div>
    <div class="lh-contact" style="top:487px;left:44px;text-align:center">Unit 4, 12th Floor<br>Quarry Lane<br>London</div>
    <div class="icon" style="left:20px;top:509px;width:15px;height:15px">
      <svg viewBox="0 0 24 24" fill="none" stroke="#fff" stroke-width="2"><circle cx="12" cy="12" r="9"/><path d="M3 12h18M12 3c3 3 3 15 0 18M12 3c-3 3-3 15 0 18"/></svg>
    </div>
    <div class="lh-contact" style="top:511px">info@fernholtrail.co.uk<br>sales@fernholtrail.co.uk</div>
  </section>

  <!-- Presentation folder -->
  <section class="sheet folder" aria-label="Presentation folder">
    <div class="strip"></div>
    <div class="brand brand--light">fernholt rail<span class="dot"></span></div>
    <div class="icon" style="left:34px;top:526px;width:22px;height:22px">
      <svg viewBox="0 0 24 24" fill="none" stroke="#fff" stroke-width="2"><circle cx="12" cy="12" r="9"/><path d="M3 12h18M12 3c3 3 3 15 0 18M12 3c-3 3-3 15 0 18"/></svg>
    </div>
    <div class="web">www.fernholtrail.co.uk</div>
  </section>

  <!-- Business card front -->
  <section class="sheet card-front" aria-label="Business card front">
    <svg width="176" height="100" viewBox="0 0 176 100" style="position:absolute;left:0;top:0">
      <path d="M0 0H70C84 0 84 18 78 26C72 34 72 44 80 50C86 56 86 64 78 72C70 80 76 92 62 100H0Z" fill="var(--charcoal)"/>
    </svg>
    <div class="card-contact" style="top:12px">020 7946 0142<br>020 7946 0143</div>
    <div class="card-contact" style="top:37px">Unit 4, 12th Floor<br>Quarry Lane<br>London</div>
    <div class="card-contact" style="top:66px">info@fernholtrail.co.uk<br>sales@fernholtrail.co.uk</div>
    <div class="icon" style="left:76px;top:13px;width:11px;height:11px">
      <svg viewBox="0 0 24 24" fill="#fff"><path d="M6.6 10.8a15 15 0 006.6 6.6l2.2-2.2c.3-.3.7-.4 1-.2 1.1.4 2.3.6 3.6.6.6 0 1 .4 1 1V20c0 .6-.4 1-1 1A17 17 0 013 4c0-.6.4-1 1-1h3.5c.6 0 1 .4 1 1 0 1.3.2 2.5.6 3.6.1.3 0 .7-.2 1z"/></svg>
    </div>
    <div class="icon" style="left:70px;top:40px;width:11px;height:11px">
      <svg viewBox="0 0 24 24" fill="#fff"><path d="M12 2a7 7 0 00-7 7c0 5 7 13 7 13s7-8 7-13a7 7 0 00-7-7zm0 9.5A2.5 2.5 0 1112 6a2.5 2.5 0 010 5.5z"/></svg>
    </div>
    <div class="icon" style="left:74px;top:67px;width:11px;height:11px">
      <svg viewBox="0 0 24 24" fill="none" stroke="#fff" stroke-width="2.4"><circle cx="12" cy="12" r="9"/><path d="M3 12h18M12 3c3 3 3 15 0 18M12 3c-3 3-3 15 0 18"/></svg>
    </div>
    <div class="brand">fernholt rail<span class="dot"></span></div>
    <div class="card-name"><strong>PETER HALLAM</strong><br>Managing Director</div>
  </section>

  <!-- Business card back -->
  <section class="sheet card-back" aria-label="Business card back">
    <div class="brand">fernholt rail<span class="dot"></span></div>
  </section>

  <!-- Compliment slip -->
  <section class="sheet slip" aria-label="Compliment slip">
    <div class="band"></div>
    <div class="brand">fernholt rail<span class="dot"></span></div>
    <div class="address">Unit 4, 12th Floor, Quarry Lane, London</div>
    <div class="icon" style="left:12px;top:178px;width:18px;height:18px">
      <svg viewBox="0 0 24 24" fill="none" stroke="#fff" stroke-width="2"><circle cx="12" cy="12" r="9"/><path d="M3 12h18M12 3c3 3 3 15 0 18M12 3c-3 3-3 15 0 18"/></svg>
    </div>
    <div class="web">www.fernholtrail.co.uk</div>
  </section>

  <!-- Envelope back -->
  <section class="sheet envelope" aria-label="Envelope back">
    <div class="flap"></div>
    <div class="web">www.fernholtrail.co.uk</div>
  </section>

</main>
</body>
</html>
```